Yoga site design

we need to design a homepage and content sections for our yoga portal

Palvenora

Palvenora is a yoga community ecosystem dedicated to the yoga enthusiasts and adopters of an active lifestyle based upon yoga and ayurvedic living. The objective of Palvenora is to expand the involvment and adoption of yoga across the communities and facilitate the profitable growth of the various stakeholders and service providers involved with the ecosystem

Site descriptor

The site will have 4 building blocks/functionalities as specified below;

1.Directory functionality wherein it would list yoga classes/events/ workshop/ retreats and show calendar by dates and place
1. when
2. where
3. what
4. who
5. cost
6. durations

2.Search functionality

a.Find a yoga class/studio close to you (location tagging/google maps)
search/show by studioname/ teacher/ Private sessions/ yoga family
1. when
2. where
3. what
4. who
5. cost

3.Content publishing capabilty

a.Micro sites studio directory/ teachers/ frequent event holders/ therapists - contributors and serviceproviders
1. words of descriprion about yourself and your business
2. an email address
3. a live web link
4. google maps
5. contact phone number
6. a logo upload
7. a picture of themselves, (we need to specify size)
8 Weekly/monthly calendar - where thay are and when

b.Topical content
• columns written by a refference or celebrity
• parts in Montly newsletter and/or downloadable

c.Monthly Newsletter

d.What is New/News/Flash Happenings on the Site

e.Community Board
a virtual meeting place on a login and username basis
• Twitter
• chat
• yoganetwork - offline community build
• find a group close to you!

4.E-commerce capability (Yoga store)
by category;
• yoga props
• yoga clothes
• Ayurvedic related products
• Books/Music/dvd
• skin/body
tickets to events -

yoga enthusiasts across multiple cities in europe and americas

• the design should not be intrusive and allow for multiple city instances to be created using the same deisgn sensibilities
• i do not need any tech coding.

```html
<!DOCTYPE html>
<html lang="en">
<head>
<meta charset="utf-8">
<title>Palvenora — Yoga for Fitness</title>
<link href="https://fonts.googleapis.com/css2?family=Arimo:wght@400;700&display=swap" rel="stylesheet">
<style>
:root{
  --page-bg:#1b2630;
  --page-bg-light:#2a3845;
  --panel:#eef0f1;
  --panel-edge:#ffffff;
  --ink:#222a30;
  --muted:#8a9196;
  --link:#5d86a6;
  --footer-text:#8c99a3;
  --footer-head:#e6ecef;
  --rule:#4a5a66;
  --nav-text:#222;
  --caption-bg:#050607;
}
*{margin:0;padding:0;box-sizing:border-box}
html,body{width:894px;height:1200px;overflow:hidden}
body{
  font-family:"Arimo",Arial,sans-serif;
  background:radial-gradient(ellipse at 50% 0%,var(--page-bg-light) 0%,var(--page-bg) 55%,#141d25 100%);
  position:relative;color:var(--ink);
}
.brand{position:absolute;top:10px;left:0;width:894px;text-align:center;color:#fff}
.brand-name{font-size:32px;font-weight:400;letter-spacing:1px;line-height:36px}
.brand-tag{font-size:8px;letter-spacing:1px;margin-top:1px}

.nav{position:absolute;left:111px;top:67px;width:678px;height:31px;border-radius:6px;
  background:linear-gradient(#ffffff,#dde1e4);display:flex;align-items:center;padding-left:12px}
.nav a{font-size:9px;font-weight:700;color:var(--nav-text);text-decoration:none;padding:0 9px;line-height:31px;letter-spacing:-.2px}
.nav a.active{background:linear-gradient(#e6eaec,#c9cfd3);color:var(--link);border-left:1px solid #c3c8cc;border-right:1px solid #c3c8cc}
.search{position:absolute;right:8px;top:7px;width:172px;height:18px;border-radius:9px;background:#2b3640;display:flex;align-items:center}
.search span{font-size:8px;color:#8c98a2;padding-left:9px;flex:1}
.search .btn{width:26px;height:18px;border-radius:0 9px 9px 0;background:linear-gradient(#f4f5f6,#cfd4d7);display:flex;align-items:center;justify-content:center}

.slider{position:absolute;left:111px;top:108px;width:678px;height:284px;border-radius:6px;overflow:hidden;background:var(--caption-bg)}
.slider-photo{position:absolute;left:0;top:0;width:678px;height:218px;
  background:linear-gradient(100deg,#c8b7a6 0%,#a88872 30%,#d9c3ae 55%,#b98d72 75%,#e7d4c3 100%)}
.slide-lines{position:absolute;left:140px;top:16px}
.slide-dots{position:absolute;left:312px;top:14px;display:flex;gap:2px}
.slide-dots i{width:6px;height:6px;border-radius:50%;background:#333;display:block}
.caption{position:absolute;left:23px;top:228px;width:560px;color:#fff}
.caption h2{font-size:13px;font-weight:700;color:#777;margin-bottom:7px}
.caption p{font-size:8px;line-height:14px;color:#ddd}

.intro{position:absolute;left:111px;top:412px;width:678px;height:57px;border-radius:6px;
  background:linear-gradient(#2e3c48,#1e2a33);box-shadow:0 0 0 1px #34424e inset}
.intro h3{position:absolute;left:29px;top:17px;font-size:13px;font-weight:400;color:#9ccbe8}
.intro p{position:absolute;left:29px;top:35px;font-size:7px;color:#5f7180}
.socials{position:absolute;right:17px;top:20px;display:flex;gap:8px}
.socials span{width:21px;height:21px;border-radius:3px;display:block}

.content{position:absolute;left:111px;top:487px;width:678px;height:437px;border-radius:6px;background:var(--panel);overflow:hidden}
.feature{position:absolute;top:17px;width:205px}
.feature h4,.product h4,.blog h4{font-size:13px;font-weight:400;color:var(--ink)}
.sub{font-size:7.5px;color:var(--muted);margin-top:3px}
.thumb{margin-top:9px;width:100%;height:68px;border:2px solid #fff;box-shadow:0 0 2px #999}
.body-text{font-size:8px;line-height:13px;color:var(--muted);margin-top:15px}
.more{font-size:8px;color:var(--link);margin-top:2px}
.divider{position:absolute;left:15px;top:226px;width:648px;height:1px;background:#cfd3d6}
.product{position:absolute;left:15px;top:243px;width:383px}
.product .thumb{height:73px}
.blog{position:absolute;left:424px;top:243px;width:240px}
.post h5{font-size:9px;font-weight:700;color:var(--link);margin-top:13px}
.post .meta{font-size:7px;font-style:italic;color:#333;margin-top:3px}
.post .meta b{font-style:italic}
.post p{font-size:8px;line-height:13px;color:var(--muted);margin-top:2px}

.footer{position:absolute;left:111px;top:937px;width:678px;height:180px;border-radius:6px 6px 0 0;
  background:linear-gradient(#25323d 0%,#1c2730 25%,#18222a 100%)}
.fcol{position:absolute;top:14px}
.fcol h6{font-size:11px;font-weight:400;color:var(--footer-head);margin-bottom:18px}
.fcol ul{list-style:none;width:100px}
.fcol li{font-size:7.5px;color:#c9d2d8;padding:4px 0 6px;border-bottom:2px solid var(--rule)}
.fcol.recent ul{width:140px}
.fcol.recent li{color:var(--footer-text);border-bottom-width:1px}
.fcol p{font-size:8px;line-height:14px;color:var(--footer-text)}
.bottombar{position:absolute;left:111px;top:1135px;width:678px;height:29px;border-radius:6px;
  background:linear-gradient(#34434f,#1a242c);box-shadow:0 0 0 1px #2c3944 inset}
</style>
</head>
<body>
<header class="brand">
  <div class="brand-name">Palvenora</div>
  <div class="brand-tag">YOGA FOR FITNESS</div>
</header>

<nav class="nav">
  <a>Home</a><a>About Us</a><a>Portfolio</a><a class="active">Pages</a><a>Blog</a><a>Contact</a>
  <div class="search"><span>Search</span><div class="btn">
    <svg width="10" height="10" viewBox="0 0 10 10"><circle cx="4" cy="4" r="3" fill="none" stroke="#667" stroke-width="1.3"/><line x1="6.2" y1="6.2" x2="9" y2="9" stroke="#667" stroke-width="1.5"/></svg>
  </div></div>
</nav>

<section class="slider">
  <div class="slider-photo" role="img" aria-label="Yoga class stretching in a bright studio"></div>
  <svg class="slide-lines" width="110" height="160" viewBox="0 0 110 160">
    <g stroke="#dfe6ec" stroke-width="2"><line x1="0" y1="0" x2="110" y2="0"/><line x1="0" y1="29" x2="110" y2="29"/><line x1="0" y1="58" x2="110" y2="58"/></g>
    <g stroke="#bbb" stroke-width="1" fill="none"><polyline points="10,12 13,15 10,18"/><polyline points="10,77 13,80 10,83"/><polyline points="10,106 13,109 10,112"/><polyline points="10,135 13,138 10,141"/></g>
  </svg>
  <div class="slide-dots"><i style="background:#ccc"></i><i></i><i></i><i></i></div>
  <div class="caption">
    <h2>Village Church In The Countrys</h2>
    <p>Lorem ipsum dolor sit amet, consectetur adipiscing elit. Vivamus sit amet mauris lectus, at bibendum lacus. Mauris risus massa, facilisis id molestie vitae, ultrices in massa. Fusce faucibus ipsum nec turpis dapibus viverra et ac mauris.</p>
  </div>
</section>

<section class="intro">
  <h3>Lorem ipsum dolor sit amet, consectetur adipisicing elit, labore et dolore magna!</h3>
  <p>Lorem ipsum dolor sit amet, massa blandit. Vitae nibh mollis mauris, mauris euismod dui diam at morbi</p>
  <div class="socials">
    <span style="background:#3b5a9a"></span><span style="background:#f08a1c"></span><span style="background:#3fb3e0"></span><span style="background:#f2f2f2"></span>
  </div>
</section>

<main class="content">
  <article class="feature" style="left:15px">
    <h4>Who we are</h4><div class="sub">Lorem ipsum dolor sit amet, massa blandit.</div>
    <div class="thumb" role="img" aria-label="Woman holding a standing pose in a home studio" style="background:linear-gradient(90deg,#c9a684,#d2477a 40%,#9b7b5c)"></div>
    <p class="body-text">Vivamus aliquet blandit rutrum. Vivamus felis velit, porta vitae dapibus quis, lacinia eget urna. Nam eget massa vel velit viverra pretium vel elementum purus.</p>
    <div class="more">» Learn more</div>
  </article>
  <article class="feature" style="left:239px">
    <h4>Easy to use</h4><div class="sub">Lorem ipsum dolor sit amet, massa blandit.</div>
    <div class="thumb" role="img" aria-label="Person balancing in an arm pose on a white background" style="background:linear-gradient(#ffffff,#eeeae6 60%,#f8f8f8)"></div>
    <p class="body-text">Vivamus aliquet blandit rutrum. Vivamus felis velit, porta vitae dapibus quis, lacinia eget urna. Nam eget massa vel velit viverra pretium vel elementum purus.</p>
    <div class="more">» Learn more</div>
  </article>
  <article class="feature" style="left:462px">
    <h4>Attention to detail</h4><div class="sub">Lorem ipsum dolor sit amet, massa blandit.</div>
    <div class="thumb" role="img" aria-label="Group practising yoga outdoors by the waterfront" style="background:linear-gradient(90deg,#8fb4dc,#e8eef4 50%,#9cc0e2)"></div>
    <p class="body-text">Vivamus felis velit, porta vitae dapibus quis, lacinia eget urna. Nam eget massa vel velit viverra pretium vel elementum purus.</p>
    <div class="more">» Learn more</div>
  </article>
  <div class="divider"></div>
  <article class="product">
    <h4>This is a featured product</h4><div class="sub">Lorem ipsum dolor sit amet, massa blandit.</div>
    <div class="thumb" role="img" aria-label="Three people meditating on a beach by the sea" style="background:linear-gradient(#c8d8ea,#9fb8cf 55%,#6d8aa4)"></div>
    <p class="body-text" style="margin-top:10px">Lorem ipsum dolor sit amet, consectetur adipiscing elit. Vivamus sit amet mauris lectus, at bibendum lacus. Mauris risus massa, facilisis id molestie vitae, ultrices in massa. Fusce faucibus ipsum nec turpis dapibus viverra et ac mauris. Mauris risus massa, facilisis id molestie vitae, ultrices in massa. Fusce faucibus ipsum nec turpis dapibus viverra et ac mauris.</p>
    <div class="more">» Learn more</div>
  </article>
  <aside class="blog">
    <h4>From the blog</h4><div class="sub">Lorem ipsum dolor sit amet, massa blandit.</div>
    <div class="post">
      <h5>Pellentesque nec augue</h5>
      <div class="meta">July 26th, 2015 | <b>5 Comments</b></div>
      <p>Lorem ipsum dolor sit amet, massa blandit. Vitae nibh mollis mauris, mauris euismod dui diam at morbi, neque ligula...</p>
    </div>
    <div class="post">
      <h5>Lorem ipsum dolor sit amet</h5>
      <div class="meta">July 26th, 20015 | <b>23 Comments</b></div>
      <p>Lorem ipsum dolor sit amet, massa blandit. Vitae nibh mollis mauris, mauris euismod dui diam at morbi, neque ligula...</p>
    </div>
  </aside>
</main>

<footer class="footer">
  <div class="fcol" style="left:22px"><h6>Blogroll</h6>
    <ul><li>Development Blog</li><li>Documentation</li><li>Plugins</li><li>Suggest Ideas</li><li>Support Forum</li></ul></div>
  <div class="fcol" style="left:163px;width:190px"><h6>Simple text widget</h6>
    <p>Lorem ipsum dolor sit amet, consectetur adipisicing elit, sed do eiusmod tempor incididunt ut labore et dolore magna ali. Ut enim ad minim veniam, quis nostrud exercitation ullamco. Lorem ipsum dolor sit amet, consectetur adipisicing elit, sed do eiusmod tempor</p></div>
  <div class="fcol recent" style="left:361px"><h6>Recent post</h6>
    <ul><li>In nec nisi quis dui volutpat.</li><li>Cras pharetra, enim id nullam.</li><li>Donec luctus egestas elit sed.</li><li>Morbi vehicula risus a nullam.</li><li style="border:none">Pellentesque sodales, odio id.</li></ul></div>
  <div class="fcol" style="left:536px"><h6 style="margin-bottom:14px">Get In Touch</h6>
    <p>Firm: Palvenora Studios<br>Address: 48 Lindenhall Row,<br>12 Brookvale<br>Phone: +140 5528 761<br>Fax: +140 5528 762<br>Email: hello@palvenora.net</p></div>
</footer>
<div class="bottombar"></div>
</body>
</html>
```